Travel video blogger needs website design

I need a website designed for my new travel video blog "Roaming Sparrow". I have only just started but need a website that is fairly simple and not too busy. I have a logo which I want on it (I have attached it to this project). I also want a link to all my other social medias on the main page (vidtrekhub, Snapwell and Palnook) and my videos as well. Here is a link to my vidtrekhub page for you to look at: https://www.vidtrekhub.net/channel/QRm4tZ8pWnE2HX57YKccd31v
As I have only just started and I am still trying to find my specific niche, again I need it to be sleek and simple that I can go in and change slightly here and there. I would like these pages on the website: About Me, Videos, Social Media, Blog, Gallery, contact me. for an example I like the look of www.theroamingkinfolk.net website.

I already have the domain and I am with Harborweb with pagecraftr.org. I just want to spend my time getting better and learning about videos then trying to create a website (I am a bit of a perfectionist when I try to do something).

Target Market(s)

Young Adults (majority females) between the ages of 18 and 30 with an interest in travelling.

Industry/Entity Type

Travel Industry

Number of Pages Required

1 page

Colors

Designer to choose colors to be used in the design.

Requirements
Must have
• A like to my Snapwell, Palnook and vidtrekhub channels on the home page
• Must be a nice, simple design
• Must have my logo on the front and name "Roaming Sparrow"
Nice to have
• A nice light, bright coloured theme
Should not have
• A dark coloured theme

```html
<!DOCTYPE html>
<html lang="en">
<head>
<meta charset="utf-8">
<title>Roaming Sparrow — Travel the world with me</title>
<link rel="stylesheet" href="https://fonts.googleapis.com/css2?family=Montserrat:wght@300;400;500;600;700&family=Great+Vibes&display=swap">
<style>
:root{
  --gold:#c9a064;
  --gold-soft:#d9b98a;
  --ink:#1c1c1c;
  --night:#0b0b0b;
  --cream:#f7f1ea;
  --paper:#ffffff;
  --grey-text:#8a8a8a;
  --map-bg:#eef0f2;
  --sans:'Montserrat', Arial, sans-serif;
  --script:'Great Vibes', cursive;
}
*{box-sizing:border-box;margin:0;padding:0}
html,body{width:1200px;height:5000px;overflow:hidden}
body{font-family:var(--sans);color:var(--ink);background:var(--paper);position:relative}
section,footer,header{position:absolute;left:0;width:1200px;overflow:hidden}
.photo{position:absolute}
a{color:inherit;text-decoration:none}

/* Hero */
.hero{top:0;height:800px}
.hero .photo{inset:0;background:linear-gradient(180deg,#4b5a4e 0%,#6f7f6a 30%,#3f6c6d 55%,#1f4c57 80%,#163a44 100%)}
.brand{position:absolute;left:85px;top:0;width:280px;height:165px;background:var(--gold-soft);border-radius:0 0 140px 140px;display:flex;align-items:center;justify-content:center;gap:12px}
.brand-dot{width:30px;height:30px;border-radius:50%;background:#fff}
.brand-name{font-weight:600;font-size:22px;color:#fff;letter-spacing:1px;text-transform:uppercase}
.follow-bar{position:absolute;right:60px;top:0;height:40px;padding:0 22px;background:var(--night);display:flex;align-items:center;gap:14px;font-size:11px;color:#fff;letter-spacing:1px;font-weight:600}
.follow-bar a{font-weight:400;color:var(--gold-soft)}
.main-nav{position:absolute;right:55px;top:56px;display:flex;gap:34px;font-size:14px;color:#fff}
.main-nav .current{border-bottom:2px solid var(--gold);padding-bottom:4px}
.hero-copy{position:absolute;top:225px;left:0;width:1200px;text-align:center;color:#fff}
.hero-copy h1{font-weight:400;font-size:40px;letter-spacing:2px}
.hero-copy p{font-family:var(--script);font-size:82px;color:var(--gold-soft);line-height:1;margin-top:6px}
.dots{position:absolute;top:735px;left:0;width:1200px;display:flex;justify-content:center;gap:10px}
.dots span{width:10px;height:10px;border-radius:50%;background:rgba(255,255,255,.5)}
.dots span:first-child{background:#fff}

/* Section titles */
.section-title{position:absolute;left:0;width:1200px;display:flex;justify-content:center;align-items:center;gap:14px;font-size:26px;font-weight:400;letter-spacing:1px;text-transform:uppercase}
.section-title .mark{width:44px;height:44px;border-radius:50%;border:2px solid currentColor}
.section-title em{font-style:normal;color:var(--gold)}

/* Videos */
.videos{top:800px;height:717px}
.videos .photo{inset:0;background:linear-gradient(100deg,#e7ecec 0%,#b7cfc8 40%,#6fb8b9 70%,#3aa6b1 100%)}
.videos .section-title{top:40px;color:#444}
.player{position:absolute;left:177px;top:133px;width:816px;height:517px;background:#111}
.player-bar{height:26px;background:#000}
.player .photo{left:0;top:26px;width:816px;height:464px;background:radial-gradient(circle at 45% 45%,#b48a72 0%,#7a6456 35%,#4c5d5c 70%,#33443f 100%)}
.play{position:absolute;left:378px;top:220px;width:60px;height:42px;background:#000;border-radius:8px;display:flex;align-items:center;justify-content:center}

/* Gallery */
.gallery{top:1517px;height:723px;background:var(--cream)}
.gallery .section-title{top:60px;color:#333}
.places{position:absolute;top:170px;left:0;width:1200px}
.place{position:absolute;width:240px;text-align:center}
.globe{width:230px;height:230px;border-radius:50%;margin:0 auto;border:6px solid #fff;box-shadow:0 0 0 3px var(--ink)}
.stand{width:4px;height:40px;background:var(--ink);margin:0 auto}
.stand-base{width:70px;height:4px;background:var(--ink);margin:0 auto}
.place h3{font-size:20px;font-weight:500;margin-top:22px}
.place p{font-size:11px;color:var(--grey-text);line-height:1.5;margin-top:10px}
.btn-dark{position:absolute;left:523px;top:623px;width:165px;height:34px;background:var(--ink);color:#fff;border-radius:17px;font-size:12px;display:flex;align-items:center;justify-content:center;gap:8px}
.btn-dark i{width:10px;height:10px;border-radius:50%;background:var(--gold)}

/* Blog */
.blog{top:2240px;height:967px}
.blog .photo{inset:0;background:linear-gradient(180deg,#4a3a22 0%,#5b4a2b 45%,#3a3020 100%)}
.blog .section-title{top:62px;color:#fff}
.card{position:absolute;width:285px;background:var(--paper);box-shadow:0 6px 18px rgba(0,0,0,.3)}
.card .thumb{width:100%}
.card-body{padding:16px 18px}
.tag{font-size:9px;color:var(--gold);letter-spacing:1px;text-transform:uppercase;font-weight:600}
.card h4{font-size:13px;font-weight:700;line-height:1.35;margin-top:8px}
.card p{font-size:10px;color:var(--grey-text);line-height:1.5;margin-top:8px}
.meta{font-size:9px;color:var(--grey-text);margin-top:12px;display:flex;gap:18px}
.card.overlay{background:none}
.card.overlay .thumb{position:absolute;inset:0;height:100%}
.card.overlay .card-body{position:absolute;left:14px;right:14px;bottom:14px;border:1px solid rgba(255,255,255,.7);color:#fff;padding:14px}
.card.overlay .meta,.card.overlay p{color:#eee}

/* About banner */
.about-banner{top:3207px;height:436px}
.about-banner .photo{inset:0;background:linear-gradient(90deg,#e9d9be 0%,#d8b98a 45%,#a87f4f 75%,#6b5334 100%)}
.about-banner blockquote{position:absolute;left:140px;top:110px;width:620px;font-family:var(--script);font-size:52px;line-height:1.15;color:#333;text-align:center}
.social-row{position:absolute;left:340px;top:300px;display:flex;gap:14px}
.social-row a{display:flex;align-items:center;gap:6px;font-size:12px;font-weight:500;color:#333}
.social-row i{width:22px;height:22px;border-radius:50%;border:2px solid #333}

/* Map */
.map{top:3643px;height:667px}
.map .photo{inset:0;background:linear-gradient(180deg,var(--map-bg),#e1e4e7)}
.pin{position:absolute}
.map-card{position:absolute;left:483px;top:167px;width:217px;background:var(--paper);box-shadow:0 4px 14px rgba(0,0,0,.2)}
.map-card .thumb{height:130px;background:linear-gradient(180deg,#7fb7cf 0%,#3f8f5a 60%,#d9c79c 100%)}
.map-card .card-body{padding:14px}

/* Passion */
.passion{top:4310px;height:250px;background:#ece6de}
.passion .photo{left:0;top:0;width:620px;height:250px;background:linear-gradient(90deg,#e2ccb1 0%,#d9b79a 50%,#ece6de 100%)}
.passion-copy{position:absolute;left:667px;top:70px;width:440px;text-align:right}
.passion-copy p{font-size:20px;color:#555;letter-spacing:1px}
.passion-copy h2{font-size:20px;font-weight:700;letter-spacing:1px;margin-top:2px}
.btn-outline{display:inline-block;margin-top:18px;border:2px solid var(--ink);padding:10px 16px;font-size:12px;font-weight:600;letter-spacing:.5px}

/* Footer */
footer{top:4560px;height:440px;background:var(--night);color:#fff}
.foot-col{position:absolute;top:107px}
.foot-col h5{font-size:16px;font-weight:700;letter-spacing:1px;margin-bottom:22px}
.foot-col p,.foot-col li{font-size:13px;line-height:1.6;color:#ddd;list-style:none}
.foot-links{display:grid;grid-template-columns:140px 100px;column-gap:10px}
.foot-col .email{border-bottom:1px solid #fff}
.copyright{position:absolute;left:0;bottom:20px;width:1200px;text-align:center;font-size:11px;color:#aaa}
</style>
</head>
<body>

<header class="hero">
  <div class="photo" role="img" aria-label="Traveller paddling a yellow kayak between limestone cliffs on green water"></div>
  <a class="brand" href="#"><span class="brand-dot"></span><span class="brand-name">Roaming Sparrow</span></a>
  <div class="follow-bar">FOLLOW US : <a href="#">Palnook</a><a href="#">Snapwell</a><a href="#">Vidtrekhub</a></div>
  <nav class="main-nav">
    <a class="current" href="#">Home</a><a href="#">About Me ▾</a><a href="#">Videos ▾</a><a href="#">Social Media ▾</a><a href="#">Blog ▾</a><a href="#">Gallery ▾</a><a href="#">Contact</a>
  </nav>
  <div class="hero-copy">
    <h1>WELCOME TO ROAMING SPARROW</h1>
    <p>Travel the world with me</p>
  </div>
  <div class="dots"><span></span><span></span><span></span></div>
</header>

<section class="videos">
  <div class="photo" role="img" aria-label="Soft backdrop of a tropical lagoon with turquoise water"></div>
  <h2 class="section-title"><span class="mark"></span>Our <em>Videos</em></h2>
  <div class="player">
    <div class="player-bar"></div>
    <div class="photo" role="img" aria-label="Video still of the travel blogger speaking to camera outdoors"></div>
    <div class="play"><svg width="16" height="18" viewBox="0 0 16 18"><path d="M2 1l13 8-13 8z" fill="#fff"/></svg></div>
  </div>
</section>

<section class="gallery">
  <h2 class="section-title"><span class="mark"></span>Our <em>Gallery</em></h2>
  <div class="places">
    <div class="place" style="left:87px">
      <div class="globe" role="img" aria-label="Camel with red saddle in the Dubai desert" style="background:linear-gradient(160deg,#e9d2a8,#c98a4a 55%,#8a3a2a)"></div>
      <div class="stand"></div><div class="stand-base"></div>
      <h3>Dubai</h3>
      <p>Golden dunes, spice markets and city lights rising over the warm desert sea.</p>
    </div>
    <div class="place" style="left:347px">
      <div class="globe" role="img" aria-label="Mountain lake and green peaks in Switzerland" style="background:linear-gradient(180deg,#7fb6df,#4f8e6a 55%,#2f5e6e)"></div>
      <div class="stand"></div><div class="stand-base"></div>
      <h3>Switzerland</h3>
      <p>Alpine lakes, quiet trails and snowy summits framed by clear blue skies.</p>
    </div>
    <div class="place" style="left:607px">
      <div class="globe" role="img" aria-label="Domed monument at dusk in New Delhi" style="background:linear-gradient(180deg,#e7799a,#b95a7c 55%,#3b2a3a)"></div>
      <div class="stand"></div><div class="stand-base"></div>
      <h3>New Delhi</h3>
      <p>Grand domes at sunset, busy bazaars and flavours worth every long journey.</p>
    </div>
    <div class="place" style="left:870px">
      <div class="globe" role="img" aria-label="Waterfront skyline under a blue sky in the Bahamas" style="background:linear-gradient(180deg,#5fa2db,#3c78b8 55%,#1d3f6a)"></div>
      <div class="stand"></div><div class="stand-base"></div>
      <h3>Bahamas</h3>
      <p>White sand, bright harbours and calm water glowing in the island sun.</p>
    </div>
  </div>
  <a class="btn-dark" href="#"><i></i>More photos</a>
</section>

<section class="blog">
  <div class="photo" role="img" aria-label="Dusky savanna landscape with trees, darkened behind the posts"></div>
  <h2 class="section-title"><span class="mark"></span><em>Blog</em> Posts</h2>

  <article class="card overlay" style="left:150px;top:167px;height:277px">
    <div class="thumb photo" role="img" aria-label="Aerial view of a green island and turquoise bay" style="background:linear-gradient(150deg,#2f7a64,#4fa89a 50%,#1f5a66)"></div>
    <div class="card-body"><div class="tag">Photography</div><h4>Five hidden bays worth the long boat ride out</h4><div class="meta"><span>2 days ago</span></div></div>
  </article>

  <article class="card" style="left:460px;top:167px">
    <div class="thumb" role="img" aria-label="Hilltop castle under a bright blue sky" style="height:180px;background:linear-gradient(180deg,#5e95d6,#8fb0cc 55%,#6a6a5a)"></div>
    <div class="card-body"><div class="tag">Photography</div><h4>A weekend among castles high above the valley</h4><p>Notes on routes, trains and the best views from every old tower wall.</p><div class="meta"><span>2 days ago</span><span>One comment</span></div></div>
  </article>

  <article class="card overlay" style="left:770px;top:167px;height:277px">
    <div class="thumb photo" role="img" aria-label="Colourful festival crowd with bright costumes" style="background:linear-gradient(150deg,#c84a7a,#e39a3a 50%,#6a4aa0)"></div>
    <div class="card-body"><div class="tag">Photography</div><h4>Colour, music and dancing at a spring festival</h4><div class="meta"><span>1 week ago</span></div></div>
  </article>

  <article class="card" style="left:150px;top:467px">
    <div class="thumb" role="img" aria-label="Carved stone temple against a blue sky" style="height:180px;background:linear-gradient(180deg,#6aa2d8,#c7894a 55%,#8a5a30)"></div>
    <div class="card-body"><div class="tag">Photography</div><h4>Old stone temples and the stories behind them</h4><p>Plan an early start, bring water and let the carved walls slow you down.</p><div class="meta"><span>3 months ago</span><span>One comment</span></div></div>
  </article>

  <article class="card overlay" style="left:460px;top:560px;height:283px">
    <div class="thumb photo" role="img" aria-label="Boat bow on a misty lake at dusk" style="background:linear-gradient(180deg,#4a6a7a,#2a4452 55%,#1a2a30)"></div>
    <div class="card-body"><div class="tag">Photography</div><h4>Slow mornings on a misty mountain lake</h4><div class="meta"><span>1 month ago</span></div></div>
  </article>

  <article class="card" style="left:770px;top:467px">
    <div class="thumb" role="img" aria-label="Camel caravan crossing desert dunes at sunset" style="height:180px;background:linear-gradient(180deg,#7ea6c8,#e0a868 55%,#b87a3a)"></div>
    <div class="card-body"><div class="tag">Photography</div><h4>Riding out to the dunes for one last sunset</h4><p>What to pack, how to pick a guide and why sunrise is worth the cold.</p><div class="meta"><span>1 month ago</span><span>One comment</span></div></div>
  </article>
</section>

<section class="about-banner">
  <div class="photo" role="img" aria-label="Hiker with backpack raising both arms on a hilltop at sunrise"></div>
  <blockquote>I'm the traveller, writer and person behind Roaming Sparrow!, a travel blog!</blockquote>
  <div class="social-row">
    <a href="#"><i></i>Palnook</a><a href="#"><i></i>Snapwell</a><a href="#"><i></i>Vidtrekhub</a>
  </div>
</section>

<section class="map">
  <div class="photo" role="img" aria-label="Pale world map marking visited places"></div>
  <svg class="pin" style="left:190px;top:367px" width="24" height="32" viewBox="0 0 24 32"><path d="M12 1C6 1 2 5.5 2 11c0 7.5 10 20 10 20s10-12.5 10-20C22 5.5 18 1 12 1z" fill="#d9a35a"/><circle cx="12" cy="11" r="4" fill="#fff"/></svg>
  <svg class="pin" style="left:375px;top:410px" width="24" height="32" viewBox="0 0 24 32"><path d="M12 1C6 1 2 5.5 2 11c0 7.5 10 20 10 20s10-12.5 10-20C22 5.5 18 1 12 1z" fill="#d9a35a"/><circle cx="12" cy="11" r="4" fill="#fff"/></svg>
  <svg class="pin" style="left:430px;top:400px" width="24" height="32" viewBox="0 0 24 32"><path d="M12 1C6 1 2 5.5 2 11c0 7.5 10 20 10 20s10-12.5 10-20C22 5.5 18 1 12 1z" fill="#d9a35a"/><circle cx="12" cy="11" r="4" fill="#fff"/></svg>
  <svg class="pin" style="left:490px;top:480px" width="24" height="32" viewBox="0 0 24 32"><path d="M12 1C6 1 2 5.5 2 11c0 7.5 10 20 10 20s10-12.5 10-20C22 5.5 18 1 12 1z" fill="#d9a35a"/><circle cx="12" cy="11" r="4" fill="#fff"/></svg>
  <svg class="pin" style="left:550px;top:460px" width="24" height="32" viewBox="0 0 24 32"><path d="M12 1C6 1 2 5.5 2 11c0 7.5 10 20 10 20s10-12.5 10-20C22 5.5 18 1 12 1z" fill="#d9a35a"/><circle cx="12" cy="11" r="4" fill="#fff"/></svg>
  <svg class="pin" style="left:740px;top:530px" width="24" height="32" viewBox="0 0 24 32"><path d="M12 1C6 1 2 5.5 2 11c0 7.5 10 20 10 20s10-12.5 10-20C22 5.5 18 1 12 1z" fill="#d9a35a"/><circle cx="12" cy="11" r="4" fill="#fff"/></svg>
  <svg class="pin" style="left:370px;top:530px" width="24" height="32" viewBox="0 0 24 32"><path d="M12 1C6 1 2 5.5 2 11c0 7.5 10 20 10 20s10-12.5 10-20C22 5.5 18 1 12 1z" fill="#d9a35a"/><circle cx="12" cy="11" r="4" fill="#fff"/></svg>
  <svg class="pin" style="left:862px;top:237px" width="24" height="32" viewBox="0 0 24 32"><path d="M12 1C6 1 2 5.5 2 11c0 7.5 10 20 10 20s10-12.5 10-20C22 5.5 18 1 12 1z" fill="#d9a35a"/><circle cx="12" cy="11" r="4" fill="#fff"/></svg>
  <div class="map-card">
    <div class="thumb" role="img" aria-label="Palm trees over a white sand beach"></div>
    <div class="card-body">
      <h4 style="font-size:12px;font-weight:700">5 Reasons to visit this place</h4>
      <p style="font-size:10px;color:var(--grey-text);line-height:1.5;margin-top:8px">Soft sand, warm water, friendly towns and the slowest sunsets you will find anywhere on the coast this year.</p>
    </div>
  </div>
</section>

<section class="passion">
  <div class="photo" role="img" aria-label="Portrait of the blogger outdoors in soft light"></div>
  <div class="passion-copy">
    <p>TRAVELLING IS MY BIGGEST PASSION</p>
    <h2>YOUR JOURNEY BEGINS WITH ME</h2>
    <a class="btn-outline" href="#">FOLLOW MY DAILY UPDATES</a>
  </div>
</section>

<footer>
  <div class="foot-col" style="left:73px;width:220px">
    <h5>ABOUT</h5>
    <p>Stories, films and photos from the road, shared by a curious traveller who is still finding her way one trip at a time.</p>
  </div>
  <div class="foot-col" style="left:360px">
    <h5>NAVIGTION</h5>
    <ul class="foot-links"><li>Home</li><li></li><li>About Me</li><li></li><li>Videos</li><li></li><li>Social Media</li><li>Gallery</li><li>Blog</li><li>Contact</li></ul>
  </div>
  <div class="foot-col" style="left:650px">
    <h5>ARCHIVES</h5>
    <ul><li>March 2014</li><li>February 2017</li><li>January 2017</li><li>December 2016</li><li>May 2016</li></ul>
  </div>
  <div class="foot-col" style="left:877px">
    <h5>OUR LOCATION</h5>
    <p>4120 Juniper Court<br>Bellhaven, Oregon 97301</p>
    <p style="margin-top:10px">+1 800 555 0142</p>
    <p style="margin-top:10px"><span class="email">hello@roamingsparrow.net</span></p>
  </div>
  <div class="copyright">© 2018 roamingsparrow. All Right Reserved</div>
</footer>

</body>
</html>
```